Birchmoor Ridge Tentstays

I am Moving from rest Qo and Kestl to host my own website to create direct bookings. I haves booking platform, I just need a website to embed it into. I want a catchy website to attract potential guests to book at my accommodation located near wollin national park in Alberta, Canada.

Here is my rest Qo links:
https://www.restqo.ca/rooms/5820461937204518362?viralityEntryPoint=1&s=76

https://www.restqo.ca/rooms/5834027715963820147?viralityEntryPoint=1&s=76

https://www.restqo.ca/rooms/5907364128850273519?viralityEntryPoint=1&s=76

https://www.restqo.ca/rooms/5862173094416628305?viralityEntryPoint=1&s=76

https://www.restqo.ca/rooms/6214590837720156491?viralityEntryPoint=1&s=76

```html
<!DOCTYPE html>
<html lang="en">
<head>
<meta charset="utf-8">
<title>Birchmoor Ridge Tentstays</title>
<link href="https://fonts.googleapis.com/css2?family=Cinzel:wght@700;800;900&family=Lato:wght@400;700&display=swap" rel="stylesheet">
<style>
:root{
  --red:#d2123f;
  --red-dark:#b30d33;
  --ink:#2b211e;
  --text:#3a3230;
  --muted:#5a5250;
  --white:#ffffff;
  --line:#e6e1df;
}
*{margin:0;padding:0;box-sizing:border-box}
html,body{width:1200px;height:5245px;overflow:hidden;background:var(--white)}
body{position:relative;font-family:'Lato',sans-serif;color:var(--text)}
.abs{position:absolute}
.display{font-family:'Cinzel',serif;font-weight:900;letter-spacing:1px;color:var(--ink)}
.btn{position:absolute;display:inline-flex;align-items:center;justify-content:center;background:var(--red);color:var(--white);border-radius:22px;font-size:14px;font-weight:400;text-decoration:none}
.rule{position:absolute;height:3px;width:56px;background:var(--red);border-radius:2px}
p.body{font-size:15px;line-height:26px;text-align:justify;color:var(--text)}

/* hero */
.hero{position:absolute;left:0;top:0;width:1200px;height:790px;
  background:linear-gradient(180deg,#243a52 0%,#3d5670 28%,#6f8499 45%,#3e5a3c 62%,#2e4528 78%,#4a3a2a 100%)}
.hero-wave{position:absolute;left:0;top:560px;width:1200px;height:240px}
.nav{position:absolute;left:112px;top:61px;width:976px;height:74px;background:var(--white);border-radius:37px;box-shadow:0 4px 16px rgba(0,0,0,.18)}
.nav .link{position:absolute;top:27px;font-size:14px;color:var(--ink);text-decoration:none}
.nav .link.active{color:var(--red);border-bottom:2px solid var(--red);padding-bottom:2px}
.nav .btn{top:15px;left:823px;width:137px;height:42px;font-size:14px;color:var(--white)}
.brand-badge{position:absolute;left:520px;top:16px;width:160px;height:160px;border-radius:50%;background:var(--white);box-shadow:0 4px 14px rgba(0,0,0,.2);display:flex;align-items:center;justify-content:center;text-align:center}
.brand-badge span{font-family:'Lato',sans-serif;font-weight:700;font-size:15px;line-height:19px;color:var(--ink);width:120px}

/* about */
.photo-circle{position:absolute;border-radius:50%;border-bottom:6px solid var(--red)}
.about-photo{left:112px;top:892px;width:428px;height:432px;background:radial-gradient(circle at 50% 30%,#9fc1e6 0%,#6d98c8 35%,#4f7a3e 60%,#7a5a3a 85%)}
.section-title{position:absolute;font-size:38px;line-height:44px}

/* stats */
.stat{position:absolute;top:1420px;width:260px;text-align:center}
.stat .num{font-family:'Lato',sans-serif;font-size:46px;line-height:54px;color:var(--red)}
.stat .lbl{font-family:'Cinzel',serif;font-weight:900;font-size:20px;letter-spacing:1.5px;color:var(--ink)}
.lake{position:absolute;left:0;top:1520px;width:1200px;height:640px;
  background:linear-gradient(180deg,#ffffff 0%,#e9eef3 10%,#b9c5cf 26%,#7c8a8e 38%,#2f4a33 50%,#2a8b8f 62%,#49b7b6 74%,#9fd6d4 88%,#ffffff 100%)}
.lake::after{content:"";position:absolute;inset:0;background:linear-gradient(90deg,rgba(255,255,255,.75) 0%,rgba(255,255,255,0) 12%,rgba(255,255,255,0) 88%,rgba(255,255,255,.75) 100%)}

/* domes */
.center{left:0;width:1200px;text-align:center}
.sub{font-size:15px;line-height:26px;color:var(--text)}
.card{position:absolute;top:2393px;width:314px;height:414px;background:var(--white);border:1px solid var(--line);border-radius:14px;box-shadow:0 2px 10px rgba(0,0,0,.12)}
.card .img{position:absolute;left:10px;top:11px;width:294px;height:203px;border-radius:10px;background:linear-gradient(180deg,#d9cbb8 0%,#c8b59b 45%,#8a6a4e 75%,#5e4636 100%)}
.card h3{position:absolute;left:18px;top:238px;width:280px;font-size:20px;line-height:29px;font-weight:400;color:var(--ink)}
.card .meta{position:absolute;left:18px;top:308px;font-size:10.5px;color:var(--text);display:flex;gap:10px;align-items:center}
.card .meta i{display:inline-block;width:10px;height:8px;background:var(--red);border-radius:2px;margin-right:4px;vertical-align:-1px}
.card .btn{left:18px;top:347px;width:136px;height:40px}
.arrow{position:absolute;top:2589px;width:32px;height:32px;border-radius:50%;background:var(--ink);display:flex;align-items:center;justify-content:center}

/* adventure */
.adventure{position:absolute;left:0;top:2807px;width:1200px;height:656px;
  background:linear-gradient(180deg,#ffffff 0%,#dfe4e8 12%,#5f7a5a 30%,#3f5a3c 48%,#8c8a82 66%,#a8a39a 82%,#ffffff 100%)}

/* comfort */
.amenity{position:absolute;top:3690px;width:260px;text-align:center}
.amenity .icon{width:76px;height:76px;margin:0 auto;border-radius:50%;border:3px solid var(--ink);display:flex;align-items:center;justify-content:center}
.amenity span{display:block;margin-top:14px;font-family:'Cinzel',serif;font-weight:900;font-size:14px;letter-spacing:1.2px;color:var(--ink)}

.park-photo{left:662px;top:3942px;width:424px;height:428px;background:linear-gradient(180deg,#2f6fc4 0%,#79a6e0 40%,#6c8660 55%,#7c8b4c 75%,#5f6a36 100%)}

/* footer */
.footer{position:absolute;left:0;top:4500px;width:1200px;height:745px}
.footer .bg{position:absolute;left:0;top:0;width:1200px;height:745px}
.f-brand{position:absolute;left:0;top:4580px;width:1200px;text-align:center}
.f-brand .mark{width:190px;height:190px;border-radius:50%;border:4px solid var(--white);margin:0 auto}
.f-brand .name{margin-top:20px;font-family:'Lato',sans-serif;font-weight:700;font-size:32px;letter-spacing:2px;color:var(--white)}
.f-col{position:absolute;top:4886px;color:var(--white)}
.f-col h4{font-size:19px;font-weight:400;margin-bottom:24px}
.f-col a{display:block;color:var(--white);text-decoration:none;font-size:13.5px;line-height:43px}
.f-col p{font-size:14.5px;line-height:29px;width:250px}
.contact-row{display:flex;gap:16px;align-items:flex-start;font-size:13.5px;line-height:25px;margin-bottom:28px}
.contact-row svg{flex:none;margin-top:4px}
.social{position:absolute;top:5103px;left:112px;display:flex;gap:18px}
.social span{display:block;width:28px;height:28px;border-radius:50%;border:2px solid var(--white)}
.social span:first-child{background:var(--red);border-color:var(--red);border-radius:6px;width:36px;height:36px;margin-top:-4px}
.copy{position:absolute;top:5218px;left:0;width:1200px;text-align:center;color:var(--white);font-size:12px}
</style>
</head>
<body>

<!-- HERO -->
<section class="hero" role="img" aria-label="Clear geodome tent on a wooden deck with red chairs under a stormy mountain sky and rainbow"></section>
<svg class="hero-wave" viewBox="0 0 1200 240" preserveAspectRatio="none" aria-hidden="true">
  <path d="M0 60 C60 40 90 110 160 120 C300 140 520 150 700 130 C880 110 1050 90 1140 70 C1170 64 1190 70 1200 80 L1200 240 L0 240Z" fill="var(--ink)"/>
  <path d="M0 80 C60 60 90 126 170 134 C320 150 520 166 700 150 C880 132 1050 108 1140 92 C1170 86 1190 92 1200 100 L1200 240 L0 240Z" fill="var(--white)"/>
</svg>

<nav class="nav">
  <a class="link active" style="left:26px" href="#">Home</a>
  <a class="link" style="left:107px" href="#">Domes</a>
  <a class="link" style="left:194px" href="#">Experiences</a>
  <a class="link" style="left:314px" href="#">About</a>
  <a class="link" style="left:621px" href="#">Gallery</a>
  <a class="link" style="left:709px" href="#">Contact Us</a>
  <a class="btn" href="#">Book Now</a>
</nav>
<div class="brand-badge"><span>Birchmoor Ridge Tentstays</span></div>

<h1 class="display abs center" style="top:222px;font-size:44px;line-height:48px;color:#fff">Where the Rockies Meet<br>Refined Comfort</h1>
<p class="abs center" style="top:326px;color:#fff;font-size:19px;line-height:28px">Experience luxury geodome stays just minutes from Wollin National Park<br>— designed for adventure by day and comfort by night.</p>
<a class="btn" href="#" style="left:531px;top:407px;width:138px;height:38px">Book Now</a>

<!-- ABOUT -->
<div class="photo-circle about-photo" role="img" aria-label="White geodome on a grassy clearing surrounded by pine trees"></div>
<h2 class="display section-title" style="left:634px;top:916px">About us</h2>
<div class="rule" style="left:636px;top:966px"></div>
<div class="abs" style="left:634px;top:995px;width:454px">
  <p class="body">Lorem ipsum dolor sit amet, consectetur adipiscing elit, sed do eiusmod tempor incididunt ut labore et dolore magna aliqua. Quis ipsum suspendisse ultrices gravida. Risus commodo viverra maecenas accumsan lacus vel facilisis.</p>
  <p class="body" style="margin-top:16px">Lorem ipsum dolor sit amet, consectetur adipiscing elit, sed do eiusmod tempor incididunt ut labore et dolore magna aliqua. Quis ipsum suspendisse ultrices gravida. Risus commodo viverra maecenas accumsan lacus vel facilisis.</p>
</div>
<a class="btn" href="#" style="left:634px;top:1253px;width:137px;height:40px">Read More</a>

<!-- STATS + LAKE -->
<div class="lake" role="img" aria-label="Turquoise mountain lake with a small forested island and rocky peaks"></div>
<div class="stat" style="left:80px"><div class="num">100+</div><div class="lbl">Happy Guests</div></div>
<div class="stat" style="left:333px"><div class="num">4.9★</div><div class="lbl">Guest Rating</div></div>
<div class="stat" style="left:592px"><div class="num">15+</div><div class="lbl">Years Hosting</div></div>
<div class="stat" style="left:858px"><div class="num">5+</div><div class="lbl">Luxury Domes</div></div>

<!-- DOMES -->
<h2 class="display section-title abs center" style="top:2236px">Our Domes</h2>
<div class="rule" style="left:572px;top:2287px"></div>
<p class="abs center sub" style="top:2310px">A cozy mountain escape featuring heated interiors, premium bedding, and private<br>outdoor seating beneath the stars.</p>

<div class="arrow" style="left:62px"><svg width="12" height="12" viewBox="0 0 12 12"><path d="M8 1 L3 6 L8 11" stroke="#fff" stroke-width="2.4" fill="none"/></svg></div>
<div class="arrow" style="left:1104px"><svg width="12" height="12" viewBox="0 0 12 12"><path d="M4 1 L9 6 L4 11" stroke="#fff" stroke-width="2.4" fill="none"/></svg></div>

<article class="card" style="left:112px">
  <div class="img" role="img" aria-label="Dome interior with bed, plaid armchairs and round window"></div>
  <h3>1 Dome - Birchmoor Ridge Tentstays</h3>
  <div class="meta"><span><i></i>4 guests</span><span><i></i>1 bedroom</span><span><i></i>2 beds</span><span><i></i>1 bath</span></div>
  <a class="btn" href="#">Book Now</a>
</article>
<article class="card" style="left:442px">
  <div class="img" role="img" aria-label="Dome interior with double bed and wooden floor"></div>
  <h3>2 Dome - Birchmoor Ridge Tentstays</h3>
  <div class="meta"><span><i></i>4 guests</span><span><i></i>1 bedroom</span><span><i></i>1 beds</span><span><i></i>1 bath</span></div>
  <a class="btn" href="#">Book Now</a>
</article>
<article class="card" style="left:772px">
  <div class="img" role="img" aria-label="Dome interior with bed, desk and chairs"></div>
  <h3>3 Dome - Birchmoor Ridge Tentstays</h3>
  <div class="meta"><span><i></i>4 guests</span><span><i></i>1 bedroom</span><span><i></i>2 beds</span><span><i></i>1 bath</span></div>
  <a class="btn" href="#">Book Now</a>
</article>

<!-- ADVENTURE -->
<section class="adventure" role="img" aria-label="Forest campsite with a washroom cabin, gravel path and lounge chairs"></section>
<h2 class="display abs center" style="top:3094px;font-size:40px;color:#fff">Adventure Starts Here</h2>
<p class="abs center" style="top:3162px;color:#fff;font-size:18px;line-height:26px">Private geodomes, breathtaking views, and peaceful mountain moments — all<br>just minutes from Wollin National Park.</p>
<a class="btn" href="#" style="left:531px;top:3254px;width:138px;height:38px">Book Now</a>

<!-- COMFORT -->
<h2 class="display section-title abs center" style="top:3524px">Stay in Comfort</h2>
<div class="rule" style="left:590px;top:3576px"></div>
<p class="abs center sub" style="top:3600px">Thoughtfully selected comforts designed to make your mountain getaway relaxing,<br>seamless, and unforgettable.</p>

<div class="amenity" style="left:96px">
  <div class="icon"><svg width="40" height="32" viewBox="0 0 40 32"><path d="M4 12 Q20 -2 36 12 M10 18 Q20 9 30 18 M15 24 Q20 20 25 24" fill="none" stroke="var(--red)" stroke-width="3.5" stroke-linecap="round"/><circle cx="20" cy="29" r="2.6" fill="var(--red)"/></svg></div>
  <span>High-Speed WiFi</span>
</div>
<div class="amenity" style="left:334px">
  <div class="icon"><svg width="36" height="36" viewBox="0 0 36 36"><path d="M18 3 V33 M5 10.5 L31 25.5 M31 10.5 L5 25.5" stroke="var(--red)" stroke-width="3.5" stroke-linecap="round"/></svg></div>
  <span>Air Conditioning</span>
</div>
<div class="amenity" style="left:579px">
  <div class="icon"><svg width="32" height="38" viewBox="0 0 32 38"><path d="M16 2 C20 10 28 14 28 24 A12 12 0 0 1 4 24 C4 18 8 15 10 10 C12 15 14 16 16 16 C15 11 14 7 16 2Z" fill="var(--red)"/></svg></div>
  <span>Indoor Fireplace</span>
</div>
<div class="amenity" style="left:831px">
  <div class="icon"><svg width="40" height="32" viewBox="0 0 40 32"><path d="M6 6 V30 M15 6 V30 M25 6 V30 M34 6 V30 M2 13 H38 M2 23 H38" stroke="var(--red)" stroke-width="3.5" stroke-linecap="round"/></svg></div>
  <span>Private Backyard</span>
</div>

<!-- MINUTES FROM PARK -->
<h2 class="display section-title" style="left:112px;top:3972px;line-height:40px;font-size:38px">Minutes from Wollin<br>National Park</h2>
<div class="rule" style="left:114px;top:4066px"></div>
<div class="abs" style="left:112px;top:4090px;width:456px">
  <p class="body">Lorem ipsum dolor sit amet, consectetur adipiscing elit, sed do eiusmod tempor incididunt ut labore et dolore magna aliqua. Quis ipsum suspendisse ultrices gravida. Risus commodo viverra maecenas accumsan lacus vel facilisis.</p>
  <p class="body" style="margin-top:16px">Lorem ipsum dolor sit amet, consectetur adipiscing elit, sed do eiusmod tempor incididunt ut labore et dolore magna aliqua. Quis ipsum suspendisse ultrices gravida.</p>
</div>
<a class="btn" href="#" style="left:114px;top:4322px;width:178px;height:40px">Explore the Area</a>
<div class="photo-circle park-photo" role="img" aria-label="Open meadow with mountains and blue sky"></div>

<!-- FOOTER -->
<footer class="footer">
  <svg class="bg" viewBox="0 0 1200 745" preserveAspectRatio="none" aria-hidden="true">
    <path d="M0 150 C20 110 60 100 120 90 C220 74 200 40 300 30 C520 10 800 10 1000 30 C1080 40 1060 80 1120 100 C1160 112 1190 130 1200 140 L1200 745 L0 745Z" fill="var(--red)"/>
    <path d="M0 168 C30 130 70 122 130 112 C230 96 210 60 310 50 C520 30 800 30 990 50 C1070 60 1050 100 1110 122 C1150 134 1190 150 1200 162 L1200 745 L0 745Z" fill="var(--ink)"/>
  </svg>
</footer>
<div class="f-brand">
  <div class="mark"></div>
  <div class="name">BIRCHMOOR RIDGE TENTSTAYS</div>
</div>

<div class="f-col" style="left:112px">
  <h4>About Us</h4>
  <p>Excepteur sint occaecat cupidatat non proident, sunt in culpa qui officia deserunt mollit anim id est laborum."</p>
</div>
<div class="f-col" style="left:445px">
  <h4>Main Links</h4>
  <a href="#">Home</a><a href="#">Our Domes</a><a href="#">Gallery</a><a href="#">Experiences</a><a href="#">About Us</a>
</div>
<div class="f-col" style="left:625px">
  <h4>Contact Us</h4>
  <div class="contact-row"><svg width="18" height="22" viewBox="0 0 18 22"><path d="M9 20 C4 14 2 11 2 8 A7 7 0 0 1 16 8 C16 11 14 14 9 20Z" fill="none" stroke="#fff" stroke-width="1.6"/><circle cx="9" cy="8" r="2.5" fill="none" stroke="#fff" stroke-width="1.6"/></svg><span>123, wollin national park in<br>Alberta, Canada .</span></div>
  <div class="contact-row" style="margin-top:36px"><svg width="18" height="18" viewBox="0 0 18 18"><path d="M3 2 L6 2 L8 6 L6 8 Q8 11 10 12 L12 10 L16 12 L16 15 Q10 17 5 12 Q1 7 3 2Z" fill="none" stroke="#fff" stroke-width="1.5"/></svg><span>+ 1 555 014 2290</span></div>
  <div class="contact-row" style="margin-top:40px"><svg width="18" height="14" viewBox="0 0 18 14"><rect x="1" y="1" width="16" height="12" fill="none" stroke="#fff" stroke-width="1.5"/><path d="M1 1 L9 8 L17 1" fill="none" stroke="#fff" stroke-width="1.5"/></svg><span>info@birchmoorridgetentstays.com</span></div>
</div>
<div class="f-col" style="left:958px">
  <h4>Other Links</h4>
  <a href="#">Check Availability</a><a href="#">Location</a><a href="#">Contact Us</a><a href="#">Terms &amp; Conditions</a><a href="#">Privacy Policy</a>
</div>

<div class="social" aria-label="Social links"><span></span><span></span><span></span></div>
<div class="copy">Copyright © 2026 Birchmoor Ridge Tentstays. All rights reserved</div>

</body>
</html>
```